From Portrait to Landscape

Take a PPT document made of 54 slide of graphs, images and text and change the orientation of each one of the 54 slides from the existing Portrait layout to the Landscape one.
All the graphics and texts (including text formatting, commas, bullet points etc.) must be kept the same but spaces are reorganized in the new Landscape orientation favoring the size of the graphs (possibily reducing the text areas).
Please, find attached the first 10 pages of the PPT document (for now, in PDF format) and a couple of sample pages of the PPT.x\

Target Market(s)

Readers of the Report (ecommerce players in Italy)

Requirements
Must have
• Graphics should be larger in the Landscape orientation than they are now in the Poirtrait one

```html
<!DOCTYPE html>
<html lang="it">
<head>
<meta charset="utf-8">
<title>Shop Digitale – Aprile 2022 – Slide landscape</title>
<link href="https://fonts.googleapis.com/css2?family=Montserrat:wght@600;700&family=Source+Sans+3:wght@400;600;700&display=swap" rel="stylesheet">
<style>
:root{
  --navy:#0c2468;
  --navy-deep:#081a4e;
  --olive:#6f8b3f;
  --olive-dark:#5b7230;
  --lime:#a8ad2c;
  --section-green:#6f8a43;
  --brown:#7a6a5a;
  --teal:#6cc3bd;
  --orange:#e2782a;
  --yellow:#f5c400;
  --red:#c7253e;
  --blue:#2a5ba8;
  --pink:#e65d7d;
  --grey-tile:#4d4d4d;
  --crimson:#b5124f;
  --text:#444;
  --light-cell:#f3f5e6;
}
*{margin:0;padding:0;box-sizing:border-box}
html,body{width:1200px;height:938px;overflow:hidden;background:#fff}
body{position:relative;font-family:"Source Sans 3",Arial,sans-serif;color:var(--text)}
.slide{position:absolute;width:371px;height:208px;background:#fff;box-shadow:0 1px 4px rgba(0,0,0,.18);overflow:hidden}
.abs{position:absolute}
.slide-head{position:absolute;left:0;top:8px;padding:0 0 1px 17px;border-bottom:.6px solid var(--olive);width:110px}
.slide-title{font:700 7px "Montserrat",sans-serif;letter-spacing:.07em;color:var(--olive);white-space:nowrap}
.slide-sub{position:absolute;left:17px;top:19px;font-size:6.6px;color:#555;white-space:nowrap}
.footer{position:absolute;left:22px;top:191px;width:328px;height:7.5px;border-radius:4px;display:flex;justify-content:space-between;align-items:center;padding:0 8px;font-size:4.2px;font-weight:700;color:#fff}
.copy{font-size:4.1px;line-height:1.3;color:var(--text)}
.copy p+p{margin-top:2.5px}
.cover{background:linear-gradient(135deg,var(--navy) 0%,var(--navy-deep) 100%)}
.cover-ring{left:104px;top:23px;width:164px;height:164px;border-radius:50%;background:radial-gradient(circle,rgba(120,150,200,.45) 55%,rgba(40,70,140,.2) 72%,transparent 73%)}
.cover-disc{left:126px;top:44px;width:120px;height:122px;border-radius:50%;background:#fff}
.cover-date{left:0;width:371px;top:58px;text-align:center;font-size:7px;color:#555}
.cover-title{left:0;width:371px;top:95px;text-align:center;font-size:11px;letter-spacing:.03em;color:#666;font-variant:small-caps}
.cover-rule{left:131px;top:110px;width:110px;border-top:.5px solid #aaa}
.cover-sub{left:0;width:371px;top:112px;text-align:center;font-size:5.6px;color:#555}
.index-title{left:32px;top:84px;font:700 11.5px "Montserrat",sans-serif;letter-spacing:.05em;line-height:1.2;color:var(--brown)}
.index-rule{left:134px;top:42px;height:120px;border-left:.6px solid var(--brown)}
.index-list{left:150px;top:41px;width:174px;list-style:none}
.index-list li{display:flex;justify-content:space-between;height:14.2px;font-size:6.3px}
.index-list li b{font-weight:700}
.index-deco{right:0;top:0;width:140px;height:208px;background:linear-gradient(120deg,transparent 40%,rgba(200,210,225,.35) 41%,rgba(230,235,242,.5) 70%,transparent 71%)}
.kpi-table{position:absolute;left:62px;top:31px;width:233px;border-collapse:collapse;font-size:4.3px}
.kpi-table th{background:var(--olive);color:#fff;text-align:left;height:9px;padding:0 4px;font-weight:700}
.kpi-table td{height:7.7px;padding:0 4px;background:var(--light-cell)}
.kpi-table td:first-child{padding-left:8px}
.notes{right:77px;top:163px;text-align:right;font-size:3.4px;line-height:1.5;color:#666}
.tile{position:absolute;color:#fff;text-align:center;font-size:3.5px;line-height:1.25;padding:1.5px 3px;box-shadow:1px 1px 0 rgba(0,0,0,.12);overflow:hidden}
.tile b{display:block;font-size:5.2px;margin-bottom:2px}
.tile i{display:block;font-style:normal;font-size:2.8px;opacity:.85;margin-top:2px}
.info-box{position:absolute;background:#eef0d8;font-size:3.3px;line-height:1.35;color:#555;overflow:hidden}
.info-box h4{background:var(--olive);color:#fff;font-size:3.6px;padding:1px 4px;font-weight:700}
.info-box div{padding:2px 4px}
.caption{position:absolute;background:#e6e6e6;font-size:3.4px;color:#666;text-align:center;line-height:1.3;padding:1px 3px}
.section-title{left:0;width:371px;top:17px;text-align:center;font:700 10.5px "Montserrat",sans-serif;letter-spacing:.07em;color:#fff}
.brand-name{font-size:7px;font-weight:600;color:#555}
.family-oval{left:237px;top:30px;width:80px;height:52px;border-radius:50%;background:var(--olive-dark);color:#fff;text-align:center;font-size:4.6px;line-height:1.3;padding:14px 10px 0}
</style>
</head>
<body>

<section class="slide cover" style="left:415px;top:35px">
  <div class="abs cover-ring" role="img" aria-label="Corona di piccole illustrazioni colorate sul tema degli acquisti digitali"></div>
  <div class="abs cover-disc"></div>
  <div class="abs cover-date">Aprile 2022</div>
  <div class="abs cover-title">Shop Digitale</div>
  <div class="abs cover-rule"></div>
  <div class="abs cover-sub">Gli acquisti digitali degli italiani</div>
</section>

<section class="slide" style="left:32px;top:254px">
  <div class="abs index-deco"></div>
  <h1 class="abs index-title">INDICE DEL<br>DOCUMENTO</h1>
  <div class="abs index-rule"></div>
  <ul class="abs index-list">
    <li style="color:var(--olive)"><span>Lo sviluppo del Shop Digitale in Italia</span><b>04</b></li>
    <li style="color:var(--blue)"><span>Il percorso verso l’acquisto</span><b>13</b></li>
    <li style="color:var(--crimson)"><span>I beni e servizi acquistati</span><b>19</b></li>
    <li style="color:var(--orange)"><span>Sistema di pagamento</span><b>24</b></li>
    <li style="color:#555"><span>Delivery &amp; download e soddisfazione</span><b>28</b></li>
    <li style="color:var(--blue)"><span>Device utilizzato nell’acquisto online</span><b>32</b></li>
    <li style="color:var(--crimson)"><span>Le soluzioni digitali nei negozi fisici</span><b>35</b></li>
    <li style="color:var(--teal)"><span>Live streaming commerce</span><b>48</b></li>
    <li style="color:#555"><span>Note metodologiche</span><b>51</b></li>
  </ul>
  <div class="footer" style="background:var(--brown)"><span>Shop Digitale - Aprile 2022</span><span>2</span></div>
</section>

<section class="slide" style="left:415px;top:254px">
  <div class="slide-head" style="border-color:var(--teal);width:165px"><div class="slide-title" style="color:var(--teal)">RETEVIA</div></div>
  <div class="slide-sub" style="color:var(--teal)">Il consorzio del Commercio Digitale Italiano</div>
  <div class="abs brand-name" style="left:20px;top:55px">Retevia</div>
  <div class="abs copy" style="left:70px;top:47px;width:128px">
    <p>Retevia, consorzio nazionale delle imprese che vendono in rete, rappresenta il comparto e-commerce italiano e partecipa al confronto con le istituzioni sulle regole del mercato digitale, sia in Italia sia a livello europeo.</p>
    <p>Il consorzio raccoglie alcune centinaia di imprese, dai grandi gruppi internazionali alle piccole aziende innovative, e costituisce una rete professionale che osserva da vicino come le nuove tecnologie cambiano i mercati, i consumi e il modo di gestire un’attività commerciale.</p>
    <p>Da molti anni il consorzio offre ai propri associati corsi, studi, casi pratici e modelli di lavoro per il digitale. Retevia aderisce all’Alleanza Europea del Retail Digitale, rete che riunisce le associazioni nazionali del commercio elettronico di diversi Paesi europei.</p>
    <p>Le principali attività con cui il consorzio opera sono: studi e ricerche sul commercio digitale</p>
  </div>
  <div class="abs copy" style="left:205px;top:47px;width:148px">
    <p>• organizzazione di incontri ed eventi dedicati all’aggiornamento e allo scambio tra professionisti<br>• tavoli di lavoro che esaminano gli aspetti economici e normativi dei principali settori del commercio digitale e i temi di innovazione più attuali<br>• confronto e rappresentanza presso le istituzioni nazionali ed europee sulle norme del mercato digitale<br>• comunicazione e divulgazione sul territorio<br>• assistenza alle imprese associate con consulenza legale, fiscale e servizi dedicati<br>• ideazione e gestione di percorsi di formazione sui temi della vendita online e della trasformazione digitale<br>• supporto all’apertura verso i mercati esteri delle imprese italiane e del Made in Italy<br>• diffusione della cultura digitale tra i cittadini e strumenti che aiutano a comprare online in sicurezza, come un marchio di garanzia che segnala i siti di vendita affidabili e di qualità.</p>
  </div>
  <div class="footer" style="background:var(--teal)"><span>Shop Digitale - Aprile 2022</span><span>3</span></div>
</section>

<section class="slide" style="left:797px;top:254px;background:var(--section-green)">
  <h2 class="abs section-title">LO SVILUPPO DELL’ECOMMERCEIN ITALIA</h2>
  <div class="abs" role="img" aria-label="Disegno a tratto bianco di un personaggio che sposta una fetta di torta grafico" style="left:95px;top:58px;width:210px;height:120px;background:rgba(255,255,255,.07);border-radius:6px"></div>
</section>

<section class="slide" style="left:32px;top:475px">
  <div class="slide-head"><div class="slide-title">L’ECOMMERCE IN ITALIA</div></div>
  <div class="slide-sub">Dimensioni e trend</div>
  <table class="kpi-table">
    <thead><tr><th>Indicatore</th><th>Valore Variaz</th><th>Pre-pandemia</th></tr></thead>
    <tbody>
      <tr><td>Utenti Internet in Italia 15+ (settimanali)</td><td>42,5 milioni</td><td>+9,6%</td></tr>
      <tr><td>Acquirenti online tra utenti Internet</td><td>77,8%</td><td>+16,9 p.p.</td></tr>
      <tr><td>Acquirenti online nel trimestre</td><td>33,3 milioni</td><td>+40,2%</td></tr>
      <tr><td>Acquirenti online abituali (una volta al mese)</td><td>23,9 milioni</td><td>+44,7%</td></tr>
      <tr><td>Acquirenti online ogni 100 abitanti</td><td>66,0</td><td>+40,2%</td></tr>
      <tr><td>Quota di acquirenti online uomini</td><td>51,9%</td><td>-0,6 p.p.</td></tr>
      <tr><td>Età media degli acquirenti online</td><td>42,2 anni</td><td>-0,8 anni</td></tr>
      <tr><td>Acquisti online nel trimestre</td><td>127,9 milioni</td><td>+45,7%</td></tr>
      <tr><td>Quota acquisti online da dispositivi mobili</td><td>55,6%</td><td>+10,2 p.p.</td></tr>
      <tr><td>Quota acquirenti online via App nel semestre</td><td>57,2%</td><td>+13,5 p.p.</td></tr>
      <tr><td>Valore mensile acquisti online nel 2021</td><td>4.950 Mio €</td><td>+33,1%</td></tr>
      <tr><td>Quota a valore degli acquisti di prodotti</td><td>73,9%</td><td>+20,8 p.p.</td></tr>
      <tr><td>Media acquisti online pro-capite nel trimestre</td><td>3,83</td><td>+3,9% Y/Y</td></tr>
      <tr><td>Valore acquisti online nel 2021</td><td>51,8 B€</td><td>+36,3% Y/Y</td></tr>
      <tr><td>Previsione valore acquisti online nel 2022</td><td>56,4 B€</td><td>+8,9% Y/Y</td></tr>
    </tbody>
  </table>
  <div class="abs notes">Gli indicatori - se non diversamente indicato - si riferiscono al mese medio del primo trimestre 2022<br>La differenza rispetto al periodo pre-pandemico confronta i dati del 2019 con quelli del 2022</div>
  <div class="footer" style="background:var(--olive)"><span>Shop Digitale - Aprile 2022</span><span>5</span></div>
</section>

<section class="slide" style="left:415px;top:475px">
  <div class="slide-head"><div class="slide-title">L’ECOMMERCE IN ITALIA</div></div>
  <div class="slide-sub">Alcuni indicatori del fenomeno</div>
  <div class="tile" style="left:50px;top:33px;width:84px;height:24px;background:var(--navy)"><b>33,3 milioni</b>Acquirenti online negli ultimi tre mesi<i>(marzo 2022)</i></div>
  <div class="tile" style="left:50px;top:59px;width:84px;height:31px;background:var(--orange)"><b>+36,3%</b>Incremento di valore eCommerce rispetto al periodo pre-pandemia<i>(2022 su 2019)</i></div>
  <div class="tile" style="left:50px;top:92px;width:84px;height:27px;background:var(--blue)"><b>31,5 milioni</b>Consegne medie mensili di prodotti acquistati online<i>(stima anno 2022)</i></div>
  <div class="tile" style="left:50px;top:121px;width:84px;height:35px;background:var(--olive)"><b>20,1%</b>Quota di acquirenti di sesso femminile negli acquisti online di Assicurazioni<i>(marzo 2022)</i></div>
  <div class="tile" style="left:50px;top:158px;width:84px;height:28px;background:var(--pink)"><b>4.700 M€</b>Valore mensile medio degli acquisti online degli italiani nel 2022<i>(marzo 2022)</i></div>
  <div class="tile" style="left:139px;top:33px;width:84px;height:28px;background:var(--grey-tile)"><b>78,6</b>Acquisti online di prodotti fisici ogni 100 acquisti online<i>(marzo 2022)</i></div>
  <div class="tile" style="left:139px;top:64px;width:84px;height:35px;background:var(--blue)"><b>57,2%</b>Quota di acquirenti online che negli ultimi sei mesi ha fatto acquisti via App su acquisti via App su<i>(marzo 2022)</i></div>
  <div class="tile" style="left:139px;top:102px;width:84px;height:32px;background:#6a6a6a"><b>14,0</b>Pacchi ritirati in un luogo fisico ogni 100 pacchi spediti per un pacchi spediti per un<i>(marzo 2022)</i></div>
  <div class="tile" style="left:139px;top:136px;width:173px;height:15px;background:var(--red);text-align:left"><span style="position:absolute;left:16px;top:2px;font-weight:700;font-size:5px">54,9%</span><span style="position:absolute;left:72px;top:2px">Acquirenti online presso un merchant sul quale si era<br>già acquistato in passato</span></div>
  <div class="tile" style="left:139px;top:154px;width:84px;height:32px;background:var(--navy)"><b>50,1</b>Acquisti originati da Smartphone ogni 100 acquisti online<i>(marzo 2022)</i></div>
  <div class="tile" style="left:228px;top:33px;width:84px;height:28px;background:#6a6a6a"><b>58,9 €</b>spesi online dalle donne ogni 100€ spesi online da tutti gli italiani<i>(marzo 2022)</i></div>
  <div class="tile" style="left:228px;top:64px;width:84px;height:26px;background:var(--olive)"><b>11,9 su 100</b>acquisti online presso merchant di retailer tradizionali<i>(marzo 2022)</i></div>
  <div class="tile" style="left:228px;top:92px;width:84px;height:40px;background:var(--orange)"><b>57</b>Età media degli acquirenti online di prodotti enogastronomici<i>(marzo 2022)</i></div>
  <div class="tile" style="left:228px;top:154px;width:84px;height:32px;background:var(--teal)"><b>1,39 milioni</b>Consegne mensili in negozio di prodotti acquistati online acquistati online<i>(marzo 2022)</i></div>
  <div class="footer" style="background:var(--navy)"><span>Shop Digitale - Aprile 2022</span><span>6</span></div>
</section>

<section class="slide" style="left:797px;top:475px">
  <div class="slide-head" style="width:168px"><div class="slide-title">LE DIMENSIONI DEL FENOMENO</div></div>
  <div class="slide-sub">La diffusione dell’esperienza di acquisto online in Italia</div>
  <svg class="abs" style="left:16px;top:48px" width="170" height="88" viewBox="0 0 170 88" font-family="Source Sans 3,sans-serif" font-size="3.6" fill="#555" role="img" aria-label="Istogramma acquirenti abituali e sporadici 2011-2022">
    <g text-anchor="end"><text x="8" y="79">0</text><text x="8" y="70.6">4</text><text x="8" y="62.3">8</text><text x="8" y="54">12</text><text x="8" y="45.6">16</text><text x="8" y="37.3">20</text><text x="8" y="29">24</text><text x="8" y="20.6">28</text><text x="8" y="12.3">32</text><text x="8" y="4">36</text></g>
    <g fill="var(--olive)">
      <rect x="13" y="67.6" width="9" height="10.4"/><rect x="25" y="65.5" width="9" height="12.5"/><rect x="37" y="63.4" width="9" height="14.6"/><rect x="49" y="61.3" width="9" height="16.7"/><rect x="61" y="61.3" width="9" height="16.7"/><rect x="73" y="59.3" width="9" height="18.7"/><rect x="85" y="57.2" width="9" height="20.8"/><rect x="97" y="55.1" width="9" height="22.9"/><rect x="109" y="53" width="9" height="25"/><rect x="121" y="46.8" width="9" height="31.2"/><rect x="133" y="34.3" width="9" height="43.7"/><rect x="145" y="28" width="9" height="50"/>
    </g>
    <g fill="var(--lime)">
      <rect x="13" y="59.3" width="9" height="8.3"/><rect x="25" y="55.1" width="9" height="10.4"/><rect x="37" y="53" width="9" height="10.4"/><rect x="49" y="51" width="9" height="10.3"/><rect x="61" y="48.9" width="9" height="12.4"/><rect x="73" y="46.8" width="9" height="12.5"/><rect x="85" y="42.6" width="9" height="14.6"/><rect x="97" y="40.5" width="9" height="14.6"/><rect x="109" y="38.4" width="9" height="14.6"/><rect x="121" y="30.1" width="9" height="16.7"/><rect x="133" y="17.6" width="9" height="16.7"/><rect x="145" y="9.3" width="9" height="18.7"/>
    </g>
    <g text-anchor="middle" font-size="3.2"><text x="17.5" y="83">2011</text><text x="29.5" y="83">2012</text><text x="41.5" y="83">2013</text><text x="53.5" y="83">2014</text><text x="65.5" y="83">2015</text><text x="77.5" y="83">2016</text><text x="89.5" y="83">2017</text><text x="101.5" y="83">2018</text><text x="113.5" y="83">2019</text><text x="125.5" y="83">2020</text><text x="137.5" y="83">2021</text><text x="149.5" y="83">2022</text></g>
    <text x="14" y="6" font-size="2.6" fill="var(--lime)">■ Sporadici 9,4 milioni (+3,2M rispetto al 2019)</text>
    <text x="14" y="12" font-size="2.6" fill="var(--olive)">■ Abituali 23,9 milioni (+7,4M rispetto al 2019)</text>
  </svg>
  <div class="caption" style="left:29px;top:139px;width:148px">Milioni di acquirenti online nel trimestre, distinti tra sporadici e abituali: negli ultimi tre anni (dal periodo pre-pandemia) gli abituali sono cresciuti tre volte tanto gli sporadici</div>
  <div class="info-box" style="left:188px;top:52px;width:85px;height:38px"><h4>Le dimensioni dell’utenza Internet italiana</h4><div>In Italia 42,5 milioni di individui di almeno 15 anni di età accedono regolarmente alla Rete almeno una volta alla settimana, da ogni luogo e utilizzando un qualsiasi device.</div></div>
  <svg class="abs" style="left:188px;top:52px" width="183" height="120" viewBox="0 0 183 120" font-family="Source Sans 3,sans-serif" font-size="3.2" fill="#555" role="img" aria-label="Cerchi concentrici dell'utenza internet e degli acquirenti online">
    <circle cx="88" cy="64" r="44" fill="#eef0d8"/>
    <circle cx="88" cy="70" r="34" fill="#cfd68a"/>
    <circle cx="88" cy="77" r="25" fill="#a8b35a"/>
    <circle cx="88" cy="86" r="16" fill="var(--olive)"/>
    <g text-anchor="middle" fill="#555"><text x="88" y="29">Universo</text><text x="88" y="33">Internet italiano</text></g>
    <g text-anchor="middle" fill="#fff"><text x="88" y="45">Acquirenti online</text><text x="88" y="49">almeno una volta</text><text x="88" y="53">nella vita</text><text x="88" y="64">Acquirenti online</text><text x="88" y="68">negli ultimi 3 mesi</text><text x="88" y="86">Acquirenti online</text><text x="88" y="90">abituali</text></g>
    <text x="123" y="11">Totale utenza Internet italiana</text><text x="132" y="16" font-weight="700">42,5 M di individui 15+</text>
    <line x1="105" y1="36" x2="183" y2="36" stroke="#999" stroke-width=".3" stroke-dasharray="1 1"/>
    <text x="130" y="47">85,0% dell’utenza Internet</text><text x="132" y="51">ovvero 36,1M di individui</text>
    <line x1="0" y1="64" x2="60" y2="64" stroke="#999" stroke-width=".3" stroke-dasharray="1 1"/>
    <text x="0" y="59">78,4% dell’utenza</text><text x="0" y="63">pari a 33,3 M di individui</text>
    <line x1="0" y1="86" x2="72" y2="86" stroke="#999" stroke-width=".3" stroke-dasharray="1 1"/>
    <text x="0" y="91">56,4% dell’universo</text><text x="0" y="95">pari a 23,9 M individui</text>
  </svg>
  <div class="footer" style="background:var(--olive)"><span>Shop Digitale - Aprile 2022</span><span>7</span></div>
</section>

<section class="slide" style="left:32px;top:694px">
  <div class="slide-head" style="width:168px"><div class="slide-title">LE DIMENSIONI DEL FENOMENO</div></div>
  <div class="slide-sub">Il numero di atti di acquisto online</div>
  <svg class="abs" style="left:48px;top:33px" width="90" height="78" viewBox="0 0 90 78" font-family="Source Sans 3,sans-serif" font-size="3.4" fill="#555" role="img" aria-label="Istogramma numero di acquisti online nel trimestre 2011-2022">
    <g text-anchor="end"><text x="7" y="70">0</text><text x="7" y="61">20</text><text x="7" y="52">40</text><text x="7" y="43">60</text><text x="7" y="34">80</text><text x="7" y="25">100</text><text x="7" y="16">120</text><text x="7" y="7">140</text></g>
    <g fill="var(--olive)">
      <rect x="10" y="60" width="5" height="9"/><rect x="16.5" y="58" width="5" height="11"/><rect x="23" y="55.5" width="5" height="13.5"/><rect x="29.5" y="53.3" width="5" height="15.7"/><rect x="36" y="49" width="5" height="20"/><rect x="42.5" y="46.5" width="5" height="22.5"/><rect x="49" y="44.3" width="5" height="24.7"/><rect x="55.5" y="42" width="5" height="27"/><rect x="62" y="39.8" width="5" height="29.2"/><rect x="68.5" y="28.5" width="5" height="40.5"/><rect x="75" y="12.8" width="5" height="56.2"/><rect x="81.5" y="12" width="5" height="57"/>
    </g>
    <rect x="44" y="40" width="24" height="22" fill="#ddd" opacity=".6"/>
    <text x="10" y="75" font-size="2.6">2011 2012 2013 2014 2015 2016 2017 2018 2019 2020 2021 2022</text>
  </svg>
  <div class="caption" style="left:52px;top:114px;width:82px;font-size:3px">Numero di acquisti online nel trimestre (in milioni) generati da acquirenti italiani su siti in Italia e all’estero</div>
  <svg class="abs" style="left:150px;top:20px" width="52" height="52" viewBox="-26 -26 52 52" font-family="Source Sans 3,sans-serif" role="img" aria-label="Torta: 78,6% prodotti fisici, 21,4% beni digitali e servizi">
    <circle r="21" fill="var(--lime)"/>
    <path d="M0 0 L0 -21 A21 21 0 0 1 20.46 -4.72 Z" fill="var(--olive-dark)"/>
    <text x="9" y="-10" font-size="3.6" fill="#fff" font-weight="700">21,4%</text>
    <text x="-16" y="6" font-size="4" fill="#fff" font-weight="700">78,6%</text>
    <text x="-12" y="-23" font-size="4" fill="var(--olive)" font-weight="700">Ultimi sei mesi</text>
  </svg>
  <div class="info-box" style="left:150px;top:75px;width:53px;height:41px"><h4>Il numero di acquisti online</h4><div>• 127 milioni di atti d’acquisto online nel I trimestre 2022<br>• +45,7% rispetto allo stesso periodo del 2019 (pre-pandemia)<br>• la quota di acquisti di prodotti prevale sui servizi quando fino al 2016 era prossima alla parità</div></div>
  <div class="info-box" style="left:219px;top:42px;width:83px;height:30px"><h4>Gli acquirenti sporadici (9,4 milioni)</h4><div>uno o due acquisti nel trimestre<br>effettuano l’11% delle transazioni del trimestre<br>scontrino medio del 29% inferiore alla media<br>generano il 9% del valore totale degli acquisti online</div></div>
  <div class="info-box" style="left:219px;top:79px;width:83px;height:29px"><h4>Gli acquirenti abituali (23,9 milioni)</h4><div>tre o più acquisti nel trimestre<br>effettuano l’89% delle transazioni del trimestre<br>scontrino medio superiore alla media (+11%)<br>generano il 91% del valore totale degli acquisti online</div></div>
  <div class="abs copy" style="left:50px;top:124px;width:266px">Gli acquirenti online italiani hanno compiuto in media 1,3 acquisti al mese primo trimestre del 2022. Il numero di acquisti online cresce in modo costante e ha superato le 100 milioni di transazioni per trimestre nel 2020. La spinta della pandemia si è protratta fino al 2021 e ora si è esaurita. Ogni 100 acquisti online, negli anni 2014-2018 il circa 60 riguardavano prodotti fisici e 40 servizi e beni digitali. Il rapporto tra prodotti e servizi è cambiato notevolmente negli ultimi tre anni e oggi si contano quasi 4 acquisti di prodotti per ogni acquisto di servizi e beni digitali. Il fenomeno è anche segnato da una chiara stagionalità, con un in favore dei prodotti nei mesi invernali e una ripresa dei servizi in primavera. La frequenza media di acquisto media è pari a 4 transazioni per acquirente attivo nel trimestre e la sua distribuzione consente di distinguere tra acquirenti abituali (persone che acquistano in media almeno una volta al mese) e acquirenti sporadici (meno di tre acquisti nel trimestre). L’eCommerce è guidato dal segmento degli acquirenti abituali: 23,9 milioni di individui (7,4 in più rispetto al periodo pre-pandemico) che generano la quasi totalità del valore dell’eCommerce italiano.</div>
  <div class="footer" style="background:var(--olive)"><span>Shop Digitale - Aprile 2022</span><span>8</span></div>
</section>

<section class="slide" style="left:415px;top:694px">
  <div class="slide-head" style="width:150px;border-color:var(--orange)"><div class="slide-title" style="color:var(--olive)">IL VALORE DEGLI ACQUISTI ONLINE</div></div>
  <div class="slide-sub">Il valore degli acquisti online sviluppato dagli italiani</div>
  <svg class="abs" style="left:62px;top:38px" width="125" height="64" viewBox="0 0 125 64" font-family="Source Sans 3,sans-serif" font-size="3.2" fill="#555" role="img" aria-label="Istogramma valore annuale acquisti online 2011-2022">
    <g text-anchor="end"><text x="7" y="58">0</text><text x="7" y="48.8">10</text><text x="7" y="39.6">20</text><text x="7" y="30.4">30</text><text x="7" y="21.2">40</text><text x="7" y="12">50</text><text x="7" y="2.8">60</text></g>
    <g fill="var(--orange)">
      <rect x="10" y="49.6" width="7" height="7.4"/><rect x="19" y="47.8" width="7" height="9.2"/><rect x="28" y="46" width="7" height="11"/><rect x="37" y="44.1" width="7" height="12.9"/><rect x="46" y="41.4" width="7" height="15.6"/><rect x="55" y="37.7" width="7" height="19.3"/><rect x="64" y="34" width="7" height="23"/><rect x="73" y="29.4" width="7" height="27.6"/><rect x="82" y="23.9" width="7" height="33.1"/><rect x="91" y="22" width="7" height="35"/><rect x="100" y="21" width="7" height="36"/><rect x="109" y="9.3" width="7" height="47.7"/><rect x="118" y="5.1" width="6" height="51.9"/>
    </g>
    <text x="10" y="62" font-size="2.4">2011 2012 2013 2014 2015 2016 2017 2018 2019 2020 2021 2022</text>
  </svg>
  <div class="caption" style="left:58px;top:104px;width:132px">Valore annuale (n Miliardi di Euro) degli acquisti online generati dagli acquirenti italiani presso Merchant italiani e stranieri</div>
  <svg class="abs" style="left:204px;top:40px" width="84" height="62" viewBox="0 0 84 62" font-family="Source Sans 3,sans-serif" font-size="3.2" fill="#555" role="img" aria-label="Istogramma valore pro-capite acquisti online">
    <g text-anchor="end"><text x="11" y="56">0 €</text><text x="11" y="43">500 €</text><text x="11" y="30">1.000 €</text><text x="11" y="17">1.500 €</text><text x="11" y="4">2.000 €</text></g>
    <g fill="var(--yellow)">
      <rect x="14" y="27.5" width="4" height="27.5"/><rect x="19" y="26.7" width="4" height="28.3"/><rect x="24" y="26" width="4" height="29"/><rect x="29" y="25" width="4" height="30"/><rect x="34" y="22.4" width="4" height="32.6"/><rect x="39" y="20" width="4" height="35"/><rect x="44" y="17.5" width="4" height="37.5"/><rect x="49" y="15" width="4" height="40"/><rect x="54" y="12.3" width="4" height="42.7"/><rect x="59" y="15.7" width="4" height="39.3"/><rect x="64" y="14" width="4" height="41"/><rect x="69" y="12.6" width="4" height="42.4"/><rect x="74" y="13" width="4" height="42"/>
    </g>
    <text x="14" y="60" font-size="2.6">2011  2013  2015  2017  2019  2021</text>
  </svg>
  <div class="caption" style="left:207px;top:104px;width:80px">Valore pro-capite degli acquisti online</div>
  <div class="abs copy" style="left:40px;top:124px;width:290px">
    <p>Nel 2022 si prevede che il valore complessivo degli acquisti online generati dagli acquirenti online italiani raggiunga la cifra di 58 miliardi di euro. La crescita del valore è stata costante dall’inizio delle rilevazioni, nel 2011, fino al 2019, intorno al 20% annuo in media. La pandemia ha generato una discontinuità e nel 2020 la crescita si è limitata a poco più del 3% sull’anno precedente. Tuttavia, il dato del 2020 è una media che si ottiene dalla forte crescita dell’eCommerce di prodotti e la significativa riduzione di servizi e beni digitali, in particolare nel settore dei trasporti e del turismo.</p>
    <p>Il valore pro-capite annuale degli acquisti online ha seguito un profilo di sviluppo diverso negli anni: è cresciuto tra il 2012 e il 2019 e poi si è stabilizzato, dopo un calo di 10% nell’anno della pandemia causato dalla consistente riduzione degli acquisti nel settore del turismo. La crescita dell’eCommerce è quindi da attribuire a due fattori: l’allargamento della base degli acquirenti e l’aumento di frequenza (abitudine) di acquisto online. La spesa media annuale degli acquirenti abituali è cinque volte quella degli sporadici.</p>
  </div>
  <div class="footer" style="background:var(--orange)"><span>Shop Digitale - Aprile 2022</span><span>9</span></div>
</section>

<section class="slide" style="left:797px;top:694px">
  <div class="slide-head" style="width:178px"><div class="slide-title">VALORE E QUOTA DEGLI ACQUISTI ONLINE</div></div>
  <div class="slide-sub">Il contributo dell’online ai volumi complessivi del retail</div>
  <svg class="abs" style="left:30px;top:33px" width="98" height="70" viewBox="0 0 98 70" font-family="Source Sans 3,sans-serif" font-size="3.4" fill="#555" role="img" aria-label="Istogramma valore annuale e linea quota servizi e beni digitali">
    <g text-anchor="end" fill="var(--olive)" font-weight="700"><text x="7" y="65">0</text><text x="7" y="54">10</text><text x="7" y="43">20</text><text x="7" y="32">30</text><text x="7" y="21">40</text><text x="7" y="10">50</text><text x="7" y="3">60</text></g>
    <g fill="var(--orange)">
      <rect x="10" y="56" width="4.5" height="8"/><rect x="16" y="54" width="4.5" height="10"/><rect x="22" y="52" width="4.5" height="12"/><rect x="28" y="50" width="4.5" height="14"/><rect x="34" y="47" width="4.5" height="17"/><rect x="40" y="43" width="4.5" height="21"/><rect x="46" y="39" width="4.5" height="25"/><rect x="52" y="34" width="4.5" height="30"/><rect x="58" y="28" width="4.5" height="36"/><rect x="64" y="26" width="4.5" height="38"/><rect x="70" y="21" width="4.5" height="43"/><rect x="76" y="7" width="4.5" height="57"/>
    </g>
    <polyline points="12,21 18,20 24,21 30,19 36,22 42,24 48,25 54,27 60,30 66,36 72,38 78,36" fill="none" stroke="var(--lime)" stroke-width=".8"/>
    <g fill="var(--orange)" font-size="2.6"><text x="85" y="5">60%</text><text x="85" y="16">48%</text><text x="85" y="27">36%</text><text x="85" y="38">24%</text><text x="85" y="49">12%</text><text x="85" y="64">0%</text></g>
    <text x="11" y="69" font-size="2.6">2011  2013  2015  2017  2019  2021</text>
  </svg>
  <div class="caption" style="left:33px;top:106px;width:88px;font-size:2.8px">Valore annuale (B€) dell’eCommerce generato dagli italiani (scala a sinistra) e quota di acquisti di servizi e beni digitali</div>
  <svg class="abs" style="left:161px;top:30px" width="52" height="52" viewBox="-26 -26 52 52" font-family="Source Sans 3,sans-serif" role="img" aria-label="Torta: 73,9% prodotti fisici, 26,1% beni digitali e servizi">
    <circle r="21" fill="var(--lime)"/>
    <path d="M0 0 L0 -21 A21 21 0 0 1 20.95 1.46 Z" fill="var(--olive-dark)"/>
    <text x="6" y="-4" font-size="3.6" fill="#fff" font-weight="700">26,1%</text>
    <text x="-12" y="13" font-size="3.6" fill="#fff" font-weight="700">73,9%</text>
    <text x="-12" y="-23" font-size="4" fill="var(--olive)" font-weight="700">Ultimi sei mesi</text>
  </svg>
  <div class="info-box" style="left:148px;top:86px;width:76px;height:29px"><h4 style="text-align:center">Valore degli acquisti 2022</h4><div>• 58 B€ nel 2022, tra i quali quasi tre su quattro per acquisti di prodotti<br>• Crescita a valore all’8,9% Y/Y<br>• La spesa in prodotti guadagna quota rispetto ai servizi</div></div>
  <div class="abs family-oval">Valore annuale dei consumi delle famiglie italiane: 700 B€<br><b>● eCommerce: 58 B€</b></div>
  <div class="abs copy" style="left:37px;top:127px;width:281px">
    <p>Dall’inizio delle rilevazioni di Shop Digitale, il numero di acquisti online di prodotti è sempre stato superiore a quello per servizi e beni digitali. Tuttavia, lo scontrino medio più elevato nel caso di acquisti di servizi ha mantenuto fino al 2019 una quota in valore quasi pari tra le due categorie, con una leggera prevalenza dei prodotti. Tale equilibrio è stato profondamente alterato dalla pandemia di Coronavirus. La domanda di prodotti è notevolmente aumentata nei mesi del primo lockdown (primavera 2020) e, allo stesso tempo, il blocco degli acquisti di viaggi e turismo ha influenzato negativamente la quota di servizi e beni digitali. Il risultato è un nuovo equilibrio che in termini di acquisti vede la quota di servizi beni digitali ridotta a poco più del 21% e in termini di valore al 26%.</p>
    <p>In definitiva, la pandemia ha stimolato 9 miliardi in più di acquisti online e sei milioni di individui si sono attivati nell’eCommerce dal 2020 al 2022. La stima di valore dell’eCommerce per il 2022 indica che l’8% dei consumi delle famiglie italiane passerà quest’anno attraverso l’online. E’ un dato quasi doppio rispetto a quello del 2017: si può affermare che negli cinque anni è cambiata la struttura del retail italiano.</p>
  </div>
  <div class="footer" style="background:var(--lime)"><span>Shop Digitale - Aprile 2022</span><span>10</span></div>
</section>

</body>
</html>
```